Carpet cleaning company wants business card

Need an exciting new fresh design for business cards for my carpet cleaning /pest control business
www.tidewellhomecare.com.au
Can design include a lined section for quoting or information? Thanks !

```html
<!DOCTYPE html>
<html lang="en">
<head>
<meta charset="utf-8">
<title>Tidewell Home Care – Business Card</title>
<link href="https://fonts.googleapis.com/css2?family=Open+Sans:wght@400;800&display=swap" rel="stylesheet">
<style>
  :root {
    --brand-blue: #0a52a0;
    --card-white: #ffffff;
    --ink-grey: #555a60;
    --rule-grey: #c9ced6;
    --backdrop: #b5b5b5;
  }
  * { margin: 0; padding: 0; box-sizing: border-box; }
  html, body {
    width: 1200px; height: 900px; overflow: hidden;
    background: var(--backdrop);
    font-family: "Open Sans", Arial, sans-serif;
  }
  .card {
    position: absolute;
    left: 363px; width: 475px; height: 271px;
    overflow: hidden;
  }
  .card--front { top: 145px; background: var(--card-white); }
  .card--back  { top: 484px; background: var(--brand-blue); }

  .brand-name {
    font-weight: 800;
    letter-spacing: -0.2px;
    white-space: nowrap;
  }
  .card--front .brand-name {
    position: absolute; left: 38px; top: 40px;
    font-size: 21px; line-height: 30px; color: var(--brand-blue);
  }
  .card--back .brand-name {
    position: absolute; left: 0; right: 0; top: 116px;
    text-align: center;
    font-size: 28px; line-height: 38px; color: var(--card-white);
  }

  .quote-lines {
    position: absolute; left: 274px; right: 38px; top: 92px;
  }
  .quote-lines span {
    display: block; height: 22px;
    border-bottom: 1px solid var(--rule-grey);
  }

  .contact-list {
    position: absolute; left: 38px; top: 193px;
    list-style: none;
  }
  .contact-list li {
    display: flex; align-items: center;
    height: 14px;
    font-size: 11.4px; line-height: 14px;
    color: var(--ink-grey);
    white-space: nowrap;
  }
  .contact-list svg {
    width: 9px; height: 9px; margin-right: 7px; flex: none;
    fill: var(--brand-blue);
  }

  .web-band {
    position: absolute; left: 274px; right: 0; top: 217px; height: 23px;
    background: var(--brand-blue);
    color: var(--card-white);
    font-size: 11.4px; line-height: 23px;
    padding-left: 16px;
    white-space: nowrap;
  }

  .tagline {
    position: absolute; left: 0; right: 0; top: 222px;
    text-align: center;
    font-size: 11.4px; line-height: 16px; color: var(--card-white);
  }
</style>
</head>
<body>

<section class="card card--front" aria-label="Front of business card">
  <div class="brand-name">Tidewell Home Care</div>

  <div class="quote-lines" aria-label="Lined area for quotes and notes">
    <span></span><span></span><span></span><span></span>
  </div>

  <ul class="contact-list">
    <li>
      <svg viewBox="0 0 10 10" aria-hidden="true"><path d="M2 1l2 2-1 1c.6 1.3 1.7 2.4 3 3l1-1 2 2-1.2 1.2C4.5 9 1 5.5.8 2.2z"/></svg>
      07 5550 2184
    </li>
    <li>
      <svg viewBox="0 0 10 10" aria-hidden="true"><path d="M2.5 0h5v10h-5zM3.5 1v7h3V1z"/></svg>
      0400 555 729
    </li>
    <li>
      <svg viewBox="0 0 10 10" aria-hidden="true"><path d="M0 2h10v6H0zM1 3l4 3 4-3v-.2H1z"/></svg>
      admin@tidewellhomecare.com.au
    </li>
  </ul>

  <div class="web-band">www.tidewellhomecare.com.au</div>
</section>

<section class="card card--back" aria-label="Back of business card">
  <div class="brand-name">Tidewell Home Care</div>
  <p class="tagline">Enjoy a Fresh, Clean Environment the Tidewell Way</p>
</section>

</body>
</html>
```